Book Cover that will be used for a series of books with the NAME changed on each.

Create a book cover from the crude picture I will upload. A solid black background with a streetlamp shining light down on a Man with a trench coat on carrying a briefcase and a revolver. This book is about a hitman, angels, etc. The first book is entitled: Two Pale Birds - The Prelude to The Marigold Ledger series. Author K.R. BLOMVEY on cover please. Thanks.

```html
<!DOCTYPE html>
<html lang="en">
<head>
<meta charset="utf-8">
<title>The Marigold Ledger — Story One: Origin</title>
<link href="https://fonts.googleapis.com/css2?family=Anton&family=Alfa+Slab+One&family=Oswald:wght@500;600&display=swap" rel="stylesheet">
<style>
  :root {
    --page-bg: #e6e6e6;
    --cover-black: #070707;
    --title-red: #e53b26;
    --title-white: #ffffff;
    --glow-core: #f3b48a;
    --glow-red: #8a2512;
    --glow-deep: #2a0a05;
  }
  * { margin: 0; padding: 0; box-sizing: border-box; }
  html, body {
    width: 865px;
    height: 1200px;
    overflow: hidden;
    background: var(--page-bg);
  }
  .cover {
    position: absolute;
    left: 57px;
    top: 0;
    width: 750px;
    height: 1200px;
    background: var(--cover-black);
    overflow: hidden;
  }
  .cover-art {
    position: absolute;
    left: 0;
    top: 500px;
    width: 750px;
    height: 640px;
    background:
      radial-gradient(ellipse 90px 130px at 330px 90px, var(--glow-core) 0%, rgba(214,110,60,0.7) 35%, rgba(0,0,0,0) 100%),
      radial-gradient(ellipse 260px 360px at 340px 250px, rgba(138,37,18,0.85) 0%, rgba(42,10,5,0.7) 55%, rgba(7,7,7,0) 100%),
      radial-gradient(ellipse 200px 80px at 260px 580px, rgba(180,90,50,0.45) 0%, rgba(7,7,7,0) 100%),
      var(--cover-black);
  }
  .title {
    position: absolute;
    left: 0;
    width: 100%;
    text-align: center;
    font-family: 'Anton', sans-serif;
    text-transform: uppercase;
    line-height: 1;
  }
  .title-top {
    top: 150px;
    font-size: 116px;
    letter-spacing: -2px;
  }
  .title-top .word-the { color: var(--title-red); margin-right: 10px; }
  .title-top .word-main { color: var(--title-white); }
  .title-bottom {
    top: 282px;
    display: flex;
    align-items: center;
    justify-content: center;
    gap: 24px;
    font-size: 106px;
    color: var(--title-red);
    letter-spacing: 3px;
  }
  .title-rule {
    width: 180px;
    height: 4px;
    background: var(--title-red);
    margin-top: 8px;
  }
  .series-label {
    position: absolute;
    right: 44px;
    top: 420px;
    font-family: 'Oswald', sans-serif;
    font-weight: 600;
    font-size: 20px;
    letter-spacing: 8px;
    color: var(--title-white);
  }
  .story-title {
    position: absolute;
    right: 44px;
    top: 448px;
    font-family: 'Alfa Slab One', serif;
    font-size: 48px;
    color: var(--title-red);
    letter-spacing: 1px;
  }
  .author {
    position: absolute;
    left: 0;
    width: 100%;
    top: 1150px;
    text-align: center;
    font-family: 'Oswald', sans-serif;
    font-weight: 600;
    font-size: 22px;
    color: var(--title-white);
    letter-spacing: 0.5px;
  }
</style>
</head>
<body>
  <main class="cover">
    <div class="cover-art" role="img" aria-label="Night alley lit by a streetlamp, a man in a trench coat and hat seen from behind, carrying a briefcase and a revolver"></div>

    <h1 class="title title-top"><span class="word-the">The</span><span class="word-main">Marigold</span></h1>
    <div class="title title-bottom">
      <span class="title-rule"></span>
      <span class="word-last">Ledger</span>
      <span class="title-rule"></span>
    </div>

    <p class="series-label">STORY ONE:</p>
    <p class="story-title">ORIGIN</p>

    <p class="author">Author K.R. BLOMVEY</p>
  </main>
</body>
</html>
```